Brenmoor Plumbing Heating and Electric

We are looking for a basic, but very beautiful and professional looking website. We would like the ability for a customer to request service through our website via a form or email that will be forwarded to us. Other then that just contact info, our history, our rates, and the services we offer.

Look at his page, it is WAY TOO BASIC, but if gives a very general base line idea: http://www.ringquickpipes.example/

http://www.pipevalet.example/norfolk/

http://www.tapwise-williamsburg.example/emergency_plumbing.html

Target Market(s)

Heating, air conditioning, plumbing, natural gas

Industry/Entity Type

Plumbing

Number of Pages Required

4 page

Requirements
Must have
• Professional looking, very high end and modern,
Nice to have
• Would like the ability for client to contact us for service through the website utilizing some type of email.

```html
<!DOCTYPE html>
<html lang="en">
<head>
<meta charset="utf-8">
<title>Brenmoor Plumbing Heating and Electric – About us</title>
<link rel="stylesheet" href="https://fonts.googleapis.com/css2?family=Noto+Serif:wght@700&family=Open+Sans:wght@400;700&display=swap">
<style>
  :root {
    --bar: #2e2e2e;
    --blue: #2a9bf5;
    --phone-blue: #1f9ad8;
    --white: #ffffff;
    --ink: #1a1a1a;
    --social-one: #4a6198;
    --social-two: #fe6a47;
    --social-three: #28c1f7;
    --photo-a: #3f4a52;
    --photo-b: #d9d9d6;
  }
  * { box-sizing: border-box; margin: 0; padding: 0; }
  html, body { width: 1200px; height: 960px; overflow: hidden; background: var(--white); }
  body { position: relative; font-family: "Open Sans", Arial, sans-serif; color: var(--ink); }

  .site-header { position: absolute; left: 0; top: 0; width: 1200px; height: 94px; background: var(--bar); }
  .brand { position: absolute; left: 40px; top: 22px; display: flex; align-items: center; gap: 10px; }
  .brand-mark { width: 46px; height: 46px; background: var(--blue); }
  .brand-name { font-weight: 700; font-size: 26px; color: var(--white); letter-spacing: -0.3px; }
  .main-nav a { position: absolute; top: 35px; font-size: 19px; color: var(--white); text-decoration: none; line-height: 26px; }
  .main-nav a.is-current { color: var(--blue); }
  .header-phone { position: absolute; left: 1010px; top: 33px; font-size: 18px; color: var(--phone-blue); }

  .story-title { position: absolute; left: 40px; top: 202px; font-family: "Noto Serif", Georgia, serif; font-weight: 700; font-size: 36px; color: var(--blue); }
  .story-text { position: absolute; left: 40px; top: 282px; width: 600px; font-size: 15px; line-height: 18px; white-space: nowrap; }
  .story-photo { position: absolute; left: 665px; top: 210px; width: 477px; height: 320px; border: 4px solid var(--blue);
    background: linear-gradient(110deg, var(--photo-a) 0%, var(--photo-a) 35%, var(--photo-b) 70%, #ededeb 100%); }

  .site-footer { position: absolute; left: 0; top: 677px; width: 1200px; height: 283px; background: var(--bar); }
  .footer-nav { position: absolute; left: 314px; top: 49px; display: flex; flex-direction: column; }
  .footer-nav a { font-size: 15px; line-height: 17px; color: var(--white); }
  .social { position: absolute; top: 52px; width: 68px; height: 68px; box-shadow: 2px 3px 6px rgba(0,0,0,0.45); }
  .social-one { left: 482px; background: var(--social-one); }
  .social-two { left: 565px; background: var(--social-two); }
  .social-three { left: 653px; background: var(--social-three); }
  .footer-phone { position: absolute; left: 887px; top: 46px; font-size: 19px; color: var(--white); }
</style>
</head>
<body>
  <header class="site-header">
    <div class="brand"><span class="brand-mark"></span><span class="brand-name">Brenmoor</span></div>
    <nav class="main-nav">
      <a href="#" style="left:390px">Home</a>
      <a href="#" class="is-current" style="left:494px">About us</a>
      <a href="#" style="left:621px">Rates</a>
      <a href="#" style="left:723px">Services</a>
    </nav>
    <div class="header-phone">(999)999-9999</div>
  </header>

  <main>
    <h1 class="story-title">Our Story</h1>
    <p class="story-text">
      Lorem ipsum dolor sit amet, consectetur adipiscing elit,<br>
      sed do eiusmod tempor incididunt ut labore et dolore magna aliqua.<br>
      Ut enim ad minim veniam, quis nostrud exercitation ullamco laboris nisi<br>
      ut aliquip ex ea commodo consequat. Duis aute irure dolor in reprehenderit<br>
      in voluptate velit esse cillum dolore eu fugiat nulla pariatur. Excepteur sint occaecat<br>
      cupidatat non proident, sunt in culpa qui officia deserunt mollit anim id est laborum.<br>
      Lorem ipsum dolor sit amet, consectetur adipiscing elit,&nbsp; sed do eiusmod tempor<br>
      incididunt ut labore et dolore magna aliqua. Ut enim ad minim veniam, quis nostrud<br>
      exercitation ullamco laboris nisi ut aliquip ex ea commodo consequat. Duis aute<br>
      &nbsp;irure dolor in reprehenderit in voluptate velit esse cillum dolore eu fugiat nulla<br>
      pariatur. Excepteur sint occaecat cupidatat non proident, sunt in culpa<br>
      qui officia deserunt mollit anim id est laborum.
    </p>
    <div class="story-photo" role="img" aria-label="Photo of an electrician in a hard hat fitting a wall socket"></div>
  </main>

  <footer class="site-footer">
    <nav class="footer-nav">
      <a href="#">home</a>
      <a href="#">about us</a>
      <a href="#">rates</a>
      <a href="#">services</a>
    </nav>
    <a href="#" class="social social-one" aria-label="Social profile one"></a>
    <a href="#" class="social social-two" aria-label="Social profile two"></a>
    <a href="#" class="social social-three" aria-label="Social profile three"></a>
    <div class="footer-phone">(999)999-9999</div>
  </footer>
</body>
</html>
```